依頼詳細
アパートのオーナー様が問合せをしたくなるデザインで
シンプルで、誠実感のあるデザイン。
記載項目
カナメリビング株式会社 岐阜県関市桜台3丁目4-27
スミカネットFC岐阜北店、スミカネットFC各務原21号店、スミカネットFC関店経営。
電話番号0575-38-4716
×
東和住まいリンク株式会社
全国で社宅代行を受託
社宅として、一括借上
サイズ
A4
ページ数
片面
希望イメージ
シンプル 複雑
単色 カラフル
暗い 明るい
日常 高級
遊び心 厳粛
未来的 伝統的
女性的 男性的
希望する色
赤系、青系
納品ファイル
補足説明
添付は会社のいままで作成したチラシ
参考にはしなくてもいいです。
会社の情報のみ参考
■ 選んだ理由

シンプルですが、買取・管理の区別がはっきりしていて分かりやすい。
色合いも、きれいです。

■ 提案者全員のお礼・コメント

この度は、お時間を割いて多数の応募ありがとうございます。
皆様のご提案はそれぞれの良さがあり、大変悩みました。
私の分かりにくい説明でも、ここまで仕上げるのは見事です。
また、機会がありましたら是非お願い致します。

```html
<!DOCTYPE html>
<html lang="ja">
<head>
<meta charset="utf-8">
<title>アパート・マンションの買取or管理 | カナメリビング株式会社</title>
<link href="https://fonts.googleapis.com/css2?family=Noto+Sans+JP:wght@400;500;700;900&display=swap" rel="stylesheet">
<style>
  :root {
    --red: #e60012;
    --ink: #333333;
    --muted: #666666;
    --line: #d9d9d9;
    --yellow: #ffe45c;
    --white: #ffffff;
  }
  * { box-sizing: border-box; margin: 0; padding: 0; }
  html, body { width: 846px; height: 1200px; overflow: hidden; background: var(--white); }
  body { font-family: "Noto Sans JP", sans-serif; color: var(--ink); }
  .flyer { position: relative; width: 846px; height: 1200px; overflow: hidden; background: var(--white); }

  /* hero */
  .hero-bg { position: absolute; left: 0; top: 0; width: 846px; height: 380px; }
  .hero-lead { position: absolute; left: 0; width: 846px; top: 26px; text-align: center; color: var(--white); font-size: 40px; font-weight: 700; letter-spacing: 2px; }
  .hero-title { position: absolute; left: 60px; top: 92px; width: 600px; height: 130px; background: var(--white); border-radius: 18px; display: flex; align-items: center; justify-content: center; color: var(--red); font-weight: 900; font-size: 104px; letter-spacing: 2px; line-height: 1; }
  .hero-title .or { font-size: 70px; margin: 0 6px; }
  .hero-sub { position: absolute; left: 60px; width: 600px; top: 240px; text-align: center; color: var(--white); font-size: 44px; font-weight: 700; letter-spacing: 3px; }
  .hero-photo { position: absolute; left: 570px; top: 215px; width: 230px; height: 270px; background: linear-gradient(180deg, #e9e4e0 0%, #3a3a3a 60%, #262626 100%); border-radius: 4px; }

  /* section heads */
  .section-head { position: absolute; left: 40px; display: flex; align-items: flex-end; gap: 18px; }
  .section-label { width: 170px; height: 82px; display: flex; align-items: center; justify-content: center; font-size: 60px; font-weight: 900; letter-spacing: 6px; }
  .section-label.solid { background: var(--red); color: var(--white); }
  .section-label.outline { border: 4px solid var(--red); color: var(--red); background: var(--white); }
  .section-caption { color: var(--red); font-size: 26px; font-weight: 700; padding-bottom: 4px; white-space: nowrap; }
  .section-caption em { font-style: normal; font-size: 40px; }
  .buy-head { top: 400px; }
  .manage-head { top: 670px; }
  .section-rule { position: absolute; left: 40px; width: 500px; height: 3px; background: var(--red); }

  /* merits */
  .merits { position: absolute; left: 40px; top: 505px; width: 766px; display: grid; grid-template-columns: repeat(4, 1fr); gap: 12px; }
  .merit { border: 2px solid var(--line); border-top: 6px solid var(--red); padding: 10px 10px 12px; height: 140px; background: var(--white); }
  .merit h3 { color: var(--red); font-size: 17px; font-weight: 700; text-align: center; margin-bottom: 8px; }
  .merit p { font-size: 13px; line-height: 1.6; color: var(--ink); }
  .merit mark { background: linear-gradient(transparent 55%, var(--yellow) 55%); color: inherit; }

  /* plans */
  .plans { position: absolute; left: 40px; top: 790px; width: 430px; list-style: none; }
  .plan { display: flex; align-items: center; height: 62px; border-bottom: 2px dotted var(--line); }
  .plan-no { width: 40px; color: var(--red); font-size: 34px; font-weight: 900; }
  .plan-name { flex: 1; }
  .plan-name strong { display: block; color: var(--red); font-size: 17px; font-weight: 700; }
  .plan-name small { display: block; font-size: 11px; color: var(--muted); line-height: 1.3; }
  .plan-fee { width: 150px; font-size: 14px; line-height: 1.4; }
  .plan-fee b { color: var(--red); font-size: 17px; }

  .point { position: absolute; left: 490px; top: 780px; width: 316px; height: 200px; border: 3px solid var(--red); border-radius: 10px; padding: 26px 16px 10px; }
  .point-tag { position: absolute; top: -20px; left: 50%; transform: translateX(-50%); background: var(--white); padding: 0 12px; color: var(--red); font-size: 30px; font-weight: 900; letter-spacing: 2px; white-space: nowrap; }
  .point p { font-size: 14px; line-height: 1.6; }
  .point .accent { color: var(--red); font-weight: 700; font-size: 16px; }
  .point .note { font-size: 10px; color: var(--muted); margin-top: 6px; line-height: 1.5; }

  /* footer */
  .contact-band { position: absolute; left: 0; top: 1000px; width: 846px; height: 120px; background: var(--red); display: flex; align-items: center; justify-content: space-between; padding: 0 40px; }
  .company-name { display: flex; align-items: center; gap: 8px; color: var(--white); font-size: 46px; font-weight: 900; letter-spacing: 2px; white-space: nowrap; line-height: 1; }
  .company-name small { display: block; font-size: 20px; font-weight: 900; line-height: 1.15; letter-spacing: 1px; }
  .phone-box { color: var(--white); text-align: right; white-space: nowrap; }
  .phone-box span { display: block; font-size: 15px; font-weight: 500; margin-bottom: 4px; }
  .phone-number { display: flex; align-items: center; justify-content: flex-end; gap: 8px; font-size: 42px; font-weight: 900; line-height: 1.1; letter-spacing: 1px; }
  .office-info { position: absolute; left: 40px; top: 1132px; width: 766px; font-size: 12.5px; line-height: 1.7; color: var(--ink); white-space: nowrap; }
</style>
</head>
<body>
<main class="flyer">
  <svg class="hero-bg" viewBox="0 0 846 380" aria-hidden="true">
    <path d="M0 0 H846 V300 Q423 400 0 300 Z" fill="var(--red)"/>
  </svg>
  <p class="hero-lead">アパート・マンションの</p>
  <h1 class="hero-title">買取<span class="or">or</span>管理</h1>
  <p class="hero-sub">お任せください！</p>
  <div class="hero-photo" role="img" aria-label="案内するスーツ姿の女性スタッフの写真"></div>

  <header class="section-head buy-head">
    <div class="section-label solid">買取</div>
    <p class="section-caption">当社買取<em>4</em>つのメリット</p>
  </header>
  <div class="section-rule" style="top:486px"></div>

  <section class="merits">
    <article class="merit"><h3>秘密厳守</h3><p>当社が直接買取のため、周囲に<mark>知られずに売却</mark>が可能です。</p></article>
    <article class="merit"><h3>適正価格</h3><p>地元相場を熟知した査定で、<mark>仲介手数料も不要</mark>です。</p></article>
    <article class="merit"><h3>実績豊富</h3><p>岐阜県内で<mark>多数の買取実績</mark>、安心してお任せください。</p></article>
    <article class="merit"><h3>早期契約決済可</h3><p>最短<mark>2週間で決済</mark>、スピード対応いたします。</p></article>
  </section>

  <header class="section-head manage-head">
    <div class="section-label outline">管理</div>
    <p class="section-caption">選べる<em>3</em>タイプ</p>
  </header>
  <div class="section-rule" style="top:756px"></div>

  <ol class="plans">
    <li class="plan"><span class="plan-no">1</span><div class="plan-name"><strong>一般管理</strong></div><div class="plan-fee">管理料：<br>収納賃料の<b>5%</b></div></li>
    <li class="plan"><span class="plan-no">2</span><div class="plan-name"><strong>サブリース</strong><small>当社が一括借上</small></div><div class="plan-fee">管理料：<br>収納賃料の<b>10%</b></div></li>
    <li class="plan"><span class="plan-no">3</span><div class="plan-name"><strong>サブリース</strong><small>東和住まいリンク株式会社の<br>社宅として一括借上</small></div><div class="plan-fee">管理料：<br><b>無料</b></div></li>
  </ol>

  <aside class="point">
    <span class="point-tag">POINT!</span>
    <p>仲介に合格があれば、3タイプ全てで<br><span class="accent">空室の賃貸保証付き！</span><br>管理委託後3ヶ月以内に満室にならない場合は、<span class="accent">当社が家賃保証！</span></p>
    <p class="note">※詳しい条件は担当者までお問い合わせください。<br>※物件の状況により対象外となる場合があります。</p>
  </aside>

  <footer>
    <div class="contact-band">
      <p class="company-name">カナメリビング<small>株式<br>会社</small></p>
      <div class="phone-box">
        <span>お問い合わせ・ご相談はお気軽に。</span>
        <p class="phone-number">
          <svg width="34" height="34" viewBox="0 0 24 24" aria-hidden="true"><path fill="var(--white)" d="M6.6 10.8a15.1 15.1 0 0 0 6.6 6.6l2.2-2.2a1 1 0 0 1 1-.25 11.4 11.4 0 0 0 3.6.57 1 1 0 0 1 1 1V20a1 1 0 0 1-1 1A17 17 0 0 1 3 4a1 1 0 0 1 1-1h3.5a1 1 0 0 1 1 1c0 1.25.2 2.45.57 3.6a1 1 0 0 1-.25 1z"/></svg>
          0575-38-4716
        </p>
      </div>
    </div>
    <div class="office-info">
      <p>岐阜県関市桜台3丁目4-27 ｜ 営業時間 09:00-18:00 ｜ 定休日 水曜日</p>
      <p>【経営】スミカネットFC岐阜北店／スミカネットFC各務原21号店／スミカネットFC関店</p>
      <p>東和住まいリンク株式会社：全国で社宅代行を受託、社宅として一括借上いたします。</p>
    </div>
  </footer>
</main>
</body>
</html>
```